Startup Drone Platform Company business card

We are needing a business card design for our employees. We are a startup drone platform. We are looking for a business card that has our logo on one side, with the employee/company details on the opposite side. We are looking for something that is very eye catching, modern, and bold.

Target Market(s)

This will target both drone pilots and drone businesses, along with all the industries that could utilize drone services (aerial video, aerial photos, inspections, 3d mapping, etc).

Industry/Entity Type

Business

```html
<!DOCTYPE html>
<html lang="en">
<head>
<meta charset="utf-8">
<title>Skyward Lift — Business Card</title>
<link href="https://fonts.googleapis.com/css2?family=Montserrat:wght@600&family=Questrial&display=swap" rel="stylesheet">
<style>
  :root {
    --ink: #2a2a2b;
    --paper: #ffffff;
    --teal: #14c4d6;
    --text-light: #f2f2f2;
    --stage: #e9e9ea;
  }
  * { margin: 0; padding: 0; box-sizing: border-box; }
  html, body { width: 1200px; height: 800px; overflow: hidden; }
  body {
    background: var(--stage);
    font-family: "Questrial", "Century Gothic", sans-serif;
    position: relative;
  }
  .card {
    position: absolute;
    left: 320px;
    width: 560px;
    height: 320px;
    border-radius: 14px;
    overflow: hidden;
    background: var(--ink);
    box-shadow: 0 6px 18px rgba(0,0,0,0.18);
  }
  .card-front { top: 50px; }
  .card-back { top: 430px; }

  .front-shape { position: absolute; inset: 0; }

  .contact {
    position: absolute;
    left: 44px;
    top: 84px;
    color: var(--text-light);
  }
  .contact-name {
    font-family: "Montserrat", sans-serif;
    font-weight: 600;
    font-size: 22px;
    color: var(--teal);
    letter-spacing: 0.3px;
  }
  .contact-role { font-size: 15px; margin-top: 2px; }
  .contact-list { list-style: none; margin-top: 22px; font-size: 15px; line-height: 22px; }
  .contact-list li { display: flex; align-items: center; gap: 10px; }
  .contact-icon { width: 14px; height: 14px; flex: none; }
  .contact-address { margin-top: 18px; font-size: 15px; line-height: 22px; }

  .front-brand {
    position: absolute;
    right: 30px;
    top: 0;
    width: 210px;
    height: 320px;
    display: flex;
    flex-direction: column;
    align-items: center;
    justify-content: center;
    gap: 18px;
  }
  .brand-dot {
    width: 64px; height: 64px;
    border-radius: 50%;
    background: var(--teal);
  }
  .brand-name {
    font-size: 24px;
    letter-spacing: 7px;
    color: var(--ink);
    text-align: center;
    line-height: 1.4;
  }

  .back-brand {
    position: absolute;
    left: 0; right: 0; top: 128px;
    text-align: center;
    color: var(--text-light);
    font-size: 28px;
    letter-spacing: 12px;
  }
  .back-web {
    position: absolute;
    left: 0; right: 0; top: 212px;
    text-align: center;
    color: var(--text-light);
    font-size: 15px;
  }
</style>
</head>
<body>

<section class="card card-front">
  <svg class="front-shape" viewBox="0 0 560 320" aria-hidden="true">
    <path d="M350 0 C 300 80, 300 230, 420 320 L 560 320 L 560 0 Z" fill="var(--teal)"/>
    <path d="M368 0 C 318 80, 326 230, 448 320 L 560 320 L 560 0 Z" fill="var(--paper)"/>
  </svg>

  <div class="contact">
    <h1 class="contact-name">JORDAN ELLIS</h1>
    <p class="contact-role">Office Manager</p>
    <ul class="contact-list">
      <li>
        <svg class="contact-icon" viewBox="0 0 14 14"><rect width="14" height="14" rx="3" fill="var(--teal)"/><rect x="4.5" y="2.5" width="5" height="9" rx="1" fill="none" stroke="var(--ink)" stroke-width="1.2"/></svg>
        555.014.2210
      </li>
      <li>
        <svg class="contact-icon" viewBox="0 0 14 14"><rect width="14" height="14" rx="3" fill="var(--teal)"/><path d="M4 3 L6 3 L6.5 5.5 L5.3 6.3 C6 7.8 6.8 8.6 8 9.2 L8.8 8 L11 8.5 L11 10.5 C7 10.5 4 7.5 4 3 Z" fill="var(--ink)"/></svg>
        555.014.2271
      </li>
      <li>
        <svg class="contact-icon" viewBox="0 0 14 14"><rect width="14" height="14" rx="3" fill="var(--teal)"/><rect x="3" y="4" width="8" height="6" fill="none" stroke="var(--ink)" stroke-width="1.1"/><path d="M3 4 L7 7.5 L11 4" fill="none" stroke="var(--ink)" stroke-width="1.1"/></svg>
        hello@skywardlift.com
      </li>
      <li>
        <svg class="contact-icon" viewBox="0 0 14 14"><rect width="14" height="14" rx="3" fill="var(--teal)"/><circle cx="7" cy="7" r="4" fill="none" stroke="var(--ink)" stroke-width="1.1"/><path d="M3 7 H11 M7 3 V11" stroke="var(--ink)" stroke-width="1"/></svg>
        www.skywardlift.com
      </li>
    </ul>
    <p class="contact-address">48 Harbor Lane, Suite 104<br>Fairview MA 02100</p>
  </div>

  <div class="front-brand">
    <span class="brand-dot" aria-hidden="true"></span>
    <p class="brand-name">SKYWARD<br>LIFT</p>
  </div>
</section>

<section class="card card-back">
  <p class="back-brand">SKYWARD LIFT</p>
  <p class="back-web">www.skywardlift.com</p>
</section>

</body>
</html>
```